Lena Hartwell Web

Lena Hartwell is a singer/songwriter that has a presence in the market for over 20 years. She currently has a website, lenahartwell.example that needs a major makeover. IT needs to be reorganized to; 1) make it more user friendly; 2) enable multi-languages including; Spanish, French, Russian, Japanese, Chinese and Portuguese; 3) enable purchases online through a storefront of promotional merchandise and music tracks. She has a logo that needs an update, as well as we currently have a business card open on PixelBazaar for input. Working to re-brand, or refresh her brand.

Lena Hartwell is the next Rosa Delmont! She has 5 platinum records, Lumen Award nominations and tours with Harold Prescott globally and is Nora Vandermeer's key backup singer for 12 years.
Updates

Some common questions have come up.  Here is some further input:

1) Colors - No specific color in mind but probably earth tones.  Although at this point we''re completely open.  Mary likes classical style, Russian, French decor.  Paris architecture. Greek, Italian textures, Goddess like symbols from the Roman Empire, or the symbols and pomp of the British monarchy.  One name on tap for the new CD is "Lanterns Over Quiet Water"
2) Example website - I have not found a new one specifically, but what I don''t like about the existing one is it is not easy to navigate.  Needs to be streamlined and easy to navigate with a storefront for merchandise and music downloads.  
3) On Logo - We''re revamping a "Global" merchandise rollout logo.  We''ve also considered possibly modifying the old english "Hartwell" family crest which signifies royalty, but have not explored that too much.  The hexagon yellow logo on her current website, I was thinking of modifying to gold (brushed - or polished?), then taking the LH lettering using a fountain pen type look there the line thickness flows with pressure on the pen, then make the gold look like a pillow, with the letter making an impression into the gold pillow.  This expands to a high quality pin, blinged up broach with diamonds imbedded for example, Global label identity, tee shirts, label tag on fashion clothing etc etc. 
 4) One thing marketing has asked us to build is a routine video blog to reach out to fans in a personal way.  Short clips of daily activity, travel prep for shows, etc. Possibly a signup/fanpage where people get emails sent back whenever anything new is posted, like a video blog, new pics, new events.  A menu to choose what you get updates on. 

Thanks, Dennis

Target Market(s)

1) Fan base in Europe, Asia, Latin America and North America
2) Movie producers seeking soundtracks
3) Private clients seeking an outstanding performer for corporate events

Industry/Entity Type

Singer

Requirements
Must have
• Better organization into smaller pages. Items critical include: 1) music tracks, 2) ClipStream links, 3) photos & Video, 4) storefront to enable online merchandise purchase 5) a way to illustrate her genre from; gospel, to rock, funk, R&B, country,

```html
<!DOCTYPE html>
<html lang="en">
<head>
<meta charset="utf-8">
<title>Lena Hartwell</title>
<link href="https://fonts.googleapis.com/css2?family=Playfair+Display:ital,wght@0,400;0,700;1,400&family=Pinyon+Script&family=Merriweather+Sans:wght@300;400&display=swap" rel="stylesheet">
<style>
  :root {
    --navy: #1d0b36;
    --plum: #4b0a42;
    --sand: #c9b47f;
    --sand-ink: #1f1a14;
    --white: #ffffff;
    --grey: #4c4b4d;
    --night: #22103a;
    --hex-fill: rgba(226, 206, 166, 0.42);
    --sepia-light: #a47e38;
    --sepia-mid: #6b4b1c;
    --sepia-dark: #241608;
  }
  * { margin: 0; padding: 0; box-sizing: border-box; }
  html, body { width: 1200px; height: 900px; overflow: hidden; background: var(--sepia-dark); }
  .page { position: relative; width: 1200px; height: 900px; overflow: hidden; }

  .hero-photo {
    position: absolute; left: 90px; top: 0; width: 1110px; height: 900px;
    background:
      radial-gradient(ellipse 320px 520px at 540px 360px, rgba(120, 90, 40, 0.55), transparent 70%),
      radial-gradient(ellipse 700px 300px at 600px 90px, rgba(190, 150, 80, 0.55), transparent 70%),
      linear-gradient(180deg, var(--sepia-light) 0%, var(--sepia-mid) 45%, var(--sepia-dark) 100%);
  }

  /* sidebar */
  .sidebar { position: absolute; left: 0; top: 0; width: 90px; height: 900px; }
  .brand {
    height: 105px; background: var(--navy);
    display: flex; align-items: center; justify-content: center; gap: 6px;
    font-family: 'Playfair Display', serif; font-size: 26px; color: var(--sand);
  }
  .brand-dot { width: 8px; height: 8px; background: var(--sand); }
  .main-nav { height: 619px; background: var(--plum); list-style: none; padding-top: 32px; }
  .main-nav li {
    height: 88px; text-align: center;
    font-family: 'Playfair Display', serif; font-size: 16px; color: var(--white);
  }
  .social {
    height: 176px; background: var(--sand); list-style: none;
    display: flex; flex-direction: column; align-items: center; justify-content: center; gap: 16px;
    font-family: 'Merriweather Sans', sans-serif; font-size: 11px; color: var(--sand-ink);
  }

  /* top bar */
  .top-controls { position: absolute; right: 0; top: 0; display: flex; height: 52px; }
  .dropdown {
    display: flex; align-items: center; justify-content: center; gap: 10px;
    font-family: 'Playfair Display', serif; font-size: 16px;
  }
  .dropdown::after { content: ""; border-left: 5px solid transparent; border-right: 5px solid transparent; border-top: 8px solid currentColor; margin-top: 3px; }
  .subscribe { width: 156px; background: var(--white); color: #222; }
  .language { width: 157px; background: var(--grey); color: #e8e8e8; }

  .artist-name {
    position: absolute; left: 180px; top: 160px; width: 930px; text-align: center;
    font-family: 'Pinyon Script', cursive; font-size: 148px; line-height: 1.2; color: var(--white);
    white-space: nowrap;
  }

  /* feature hexagons */
  .features { position: absolute; left: 183px; top: 441px; display: flex; gap: 14px; }
  .feature { position: relative; width: 222px; height: 272px; text-align: center; color: var(--white); }
  .feature svg { position: absolute; inset: 0; }
  .feature-body { position: relative; padding-top: 58px; }
  .feature h2 { font-family: 'Playfair Display', serif; font-weight: 400; font-size: 29px; line-height: 1; }
  .rule { width: 38px; height: 2px; background: var(--white); margin: 16px auto 12px; }
  .feature p { font-family: 'Merriweather Sans', sans-serif; font-weight: 300; font-size: 16px; line-height: 20.5px; padding: 0 16px; }
  .feature .rule.bottom { margin-top: 16px; }
  .arrow { position: absolute; top: 556px; }
  .arrow.prev { left: 135px; }
  .arrow.next { left: 1121px; }

  /* player */
  .footer-band {
    position: absolute; left: 172px; top: 725px; width: 948px; height: 175px;
    background: linear-gradient(180deg, rgba(34, 16, 58, 0.96) 0%, rgba(34, 16, 58, 0.85) 100%);
  }
  .player {
    position: absolute; left: 182px; top: 740px; width: 927px; height: 71px;
    border: 1px solid rgba(255,255,255,0.45); display: flex;
  }
  .control { width: 76px; height: 69px; border-right: 1px solid rgba(255,255,255,0.45); display: flex; align-items: center; justify-content: center; }
  .track { position: absolute; left: 236px; top: 6px; width: 684px; height: 56px; background: var(--white); padding: 6px 8px; font-family: 'Playfair Display', serif; font-size: 15px; color: #222; }
  .track strong { font-weight: 700; }
  .progress { position: absolute; left: 8px; right: 8px; top: 34px; display: flex; align-items: center; gap: 8px; font-family: 'Merriweather Sans', sans-serif; font-size: 12px; color: #333; }
  .bar { flex: 1; height: 11px; background: #b3b3b3; position: relative; }
  .bar-fill { position: absolute; left: 0; top: 0; width: 58px; height: 11px; background: #6b6b6b; }
  .bar-knob { position: absolute; left: 58px; top: -3px; width: 4px; height: 17px; background: #555; }
  .copyright { position: absolute; left: 186px; top: 871px; font-family: 'Merriweather Sans', sans-serif; font-weight: 300; font-size: 14px; color: #e6e0ea; }
</style>
</head>
<body>
<div class="page">
  <div class="hero-photo" role="img" aria-label="Warm sepia concert photograph of the singer performing on stage with blurred stage lights"></div>

  <aside class="sidebar">
    <div class="brand"><span class="brand-dot"></span>LH</div>
    <ul class="main-nav">
      <li>Music</li><li>Tickets</li><li>Gallery</li><li>Store</li><li>Blog</li><li>About</li><li>Contact</li>
    </ul>
    <ul class="social">
      <li>Circlebook</li><li>Chirper</li><li>ClipStream</li>
    </ul>
  </aside>

  <div class="top-controls">
    <div class="dropdown subscribe">Subscribe</div>
    <div class="dropdown language">Language</div>
  </div>

  <h1 class="artist-name">Lena Hartwell</h1>

  <svg class="arrow prev" width="38" height="42" viewBox="0 0 38 42"><polyline points="36,1 2,21 36,41" fill="none" stroke="#fff" stroke-width="2"/></svg>
  <div class="features">
    <section class="feature">
      <svg width="222" height="272" viewBox="0 0 222 272"><polygon points="111,0 222,68 222,204 111,272 0,204 0,68" fill="var(--hex-fill)"/></svg>
      <div class="feature-body"><h2>Music</h2><div class="rule"></div><p>Lorem ipsum dolor sit amet, consectetur adipiscing elit eros quis, tincidunt</p><div class="rule bottom"></div></div>
    </section>
    <section class="feature">
      <svg width="222" height="272" viewBox="0 0 222 272"><polygon points="111,0 222,68 222,204 111,272 0,204 0,68" fill="var(--hex-fill)"/></svg>
      <div class="feature-body"><h2>Tickets</h2><div class="rule"></div><p>Lorem ipsum dolor sit amet, consectetur adipiscing elit eros quis, tincidunt</p><div class="rule bottom"></div></div>
    </section>
    <section class="feature">
      <svg width="222" height="272" viewBox="0 0 222 272"><polygon points="111,0 222,68 222,204 111,272 0,204 0,68" fill="var(--hex-fill)"/></svg>
      <div class="feature-body"><h2>Blog</h2><div class="rule"></div><p>Lorem ipsum dolor sit amet, consectetur adipiscing elit eros quis, tincidunt</p><div class="rule bottom"></div></div>
    </section>
    <section class="feature">
      <svg width="222" height="272" viewBox="0 0 222 272"><polygon points="111,0 222,68 222,204 111,272 0,204 0,68" fill="var(--hex-fill)"/></svg>
      <div class="feature-body"><h2>Store</h2><div class="rule"></div><p>Lorem ipsum dolor sit amet, consectetur adipiscing elit eros quis, tincidunt</p><div class="rule bottom"></div></div>
    </section>
  </div>
  <svg class="arrow next" width="38" height="42" viewBox="0 0 38 42"><polyline points="2,1 36,21 2,41" fill="none" stroke="#fff" stroke-width="2"/></svg>

  <div class="footer-band"></div>
  <div class="player">
    <div class="control"><svg width="36" height="18" viewBox="0 0 36 18"><rect x="1" y="1" width="4" height="16" fill="#fff"/><polygon points="19,1 19,17 6,9" fill="#fff"/><polygon points="33,1 33,17 20,9" fill="#fff"/></svg></div>
    <div class="control"><svg width="16" height="18" viewBox="0 0 16 18"><polygon points="1,1 15,9 1,17" fill="#fff"/></svg></div>
    <div class="control"><svg width="30" height="18" viewBox="0 0 30 18"><polygon points="1,1 15,9 1,17" fill="#fff"/><rect x="18" y="1" width="4" height="16" fill="#fff"/><rect x="25" y="1" width="4" height="16" fill="#fff"/></svg></div>
    <div class="track">
      <strong>Lena Hartwell</strong> - Lena Hartwell - <em>Responsible</em>
      <div class="progress"><span>0:00</span><div class="bar"><div class="bar-fill"></div><div class="bar-knob"></div></div><span>0:00</span></div>
    </div>
  </div>
  <p class="copyright">© 2014 - All Rights Reserved, Lena Hartwell</p>
</div>
</body>
</html>
```